Birchwood Clover Business Cards

I need a business card with my logo, number, Facebook account, and some information about what I am selling. Green card with logo on the front. 555-218-3946 phone number, @birchwoodclover Facebook, •Orchardgrass Hay •Alfalfa Hay •Mixed Grass Hay , and “Premium Quality Hay” all written on the back.

Target Market(s)

Hay

Contact Information for Business Card

Phone number, Facebook, different types of hay.

Colors
00AB8E
00BBA5
67D7C9
C6EFE9
E9F9F6

```html
<!DOCTYPE html>
<html lang="en">
<head>
<meta charset="utf-8">
<title>Birchwood Clover Business Cards</title>
<link href="https://fonts.googleapis.com/css2?family=Roboto:wght@400;500;700&display=swap" rel="stylesheet">
<style>
  :root {
    --page-bg: #e6e8e7;
    --brand-green: #0fa14b;
    --card-white: #f7f7f5;
    --ink: #141414;
    --band-black: #0c0c0c;
    --paper-white: #ffffff;
  }
  * { box-sizing: border-box; margin: 0; padding: 0; }
  html, body {
    width: 1200px;
    height: 874px;
    overflow: hidden;
    background: var(--page-bg);
    font-family: "Roboto", Arial, sans-serif;
  }
  .sheet {
    position: relative;
    width: 1200px;
    height: 874px;
  }
  .card {
    position: absolute;
    left: 250px;
    width: 700px;
    height: 400px;
    border-radius: 22px;
    overflow: hidden;
    box-shadow: 0 10px 28px rgba(0, 0, 0, 0.22);
  }

  /* Front */
  .card-front {
    top: 20px;
    background: var(--brand-green);
    color: var(--paper-white);
  }
  .front-brand {
    position: absolute;
    top: 70px;
    left: 0;
    width: 100%;
    display: flex;
    flex-direction: column;
    align-items: center;
    gap: 18px;
  }
  .front-brand .brand-dot {
    width: 120px;
    height: 120px;
    border-radius: 50%;
    background: var(--paper-white);
  }
  .front-brand .brand-name {
    font-size: 34px;
    font-weight: 700;
    color: var(--paper-white);
  }
  .product-list {
    position: absolute;
    left: 0;
    width: 100%;
    top: 290px;
    text-align: center;
    font-size: 19px;
    line-height: 1.3;
  }
  .product-list .rule {
    width: 340px;
    height: 1.5px;
    margin: 5px auto;
    background: var(--paper-white);
  }

  /* Back */
  .card-back {
    top: 454px;
    background: var(--card-white);
    color: var(--ink);
  }
  .back-brand {
    position: absolute;
    left: 70px;
    top: 90px;
    display: flex;
    align-items: center;
    gap: 24px;
  }
  .back-brand .brand-dot {
    width: 130px;
    height: 130px;
    border-radius: 50%;
    background: var(--brand-green);
    flex: none;
  }
  .back-brand .brand-text {
    display: flex;
    flex-direction: column;
    gap: 14px;
  }
  .back-brand .brand-name {
    font-size: 36px;
    font-weight: 700;
  }
  .back-brand .phone {
    font-family: Arial, "Roboto", sans-serif;
    font-size: 48px;
    font-weight: 700;
    letter-spacing: 0.5px;
  }
  .footer-band {
    position: absolute;
    left: 0;
    bottom: 0;
    width: 700px;
    height: 86px;
  }
  .social {
    position: absolute;
    left: 190px;
    bottom: 26px;
    display: flex;
    align-items: center;
    gap: 10px;
    color: var(--paper-white);
    font-size: 20px;
    font-weight: 500;
  }
  .social .social-dot {
    width: 22px;
    height: 22px;
    border-radius: 50%;
    background: var(--paper-white);
  }
</style>
</head>
<body>
<main class="sheet">

  <section class="card card-front" aria-label="Card front">
    <div class="front-brand">
      <span class="brand-dot"></span>
      <span class="brand-name">Birchwood Clover</span>
    </div>
    <div class="product-list">
      <p>Orchardgrass Hay • Alfalfa Hay</p>
      <div class="rule"></div>
      <p>Mixed Grass Hay, &amp; Premium Quality Hay</p>
    </div>
  </section>

  <section class="card card-back" aria-label="Card back">
    <div class="back-brand">
      <span class="brand-dot"></span>
      <div class="brand-text">
        <span class="brand-name">Birchwood Clover</span>
        <span class="phone">555-218-3946</span>
      </div>
    </div>

    <svg class="footer-band" viewBox="0 0 700 86" aria-hidden="true">
      <polygon points="0,0 540,0 512,86 0,86" fill="var(--band-black)"/>
      <polygon points="552,0 700,0 700,86 524,86" fill="var(--brand-green)"/>
    </svg>
    <div class="social">
      <span class="social-dot"></span>
      <span class="handle">@birchwoodclover</span>
    </div>
  </section>

</main>
</body>
</html>
```